Professional business cards for our auto wholesale dealership.

Target Market(s)

New and used cars sales managers and middle class to higher end private party buyers.

Industry/Entity Type

Automotive

Contact Information for Business Card

Bayline Premier Motors
Marcus T Holloway
Owner
(555) 417-3860
baypremmotors@mailbox-example.net
Dealer Lic # 48261

Logo Text

Bayline Premier Motors, Bay Prem Motors, BPM, etc

Font styles to use
Serif
Sans Serif

Colors

Designer to choose colors to be used in the design.

Requirements
Must have
• A professional, but not pretentious, look
Nice to have
• It might be nice to see "BPM" in a shape form i.e. circle, triangle, etc in the corner or background somehwere
Should not have
• bright "girly" colors

```html
<!DOCTYPE html>
<html lang="en">
<head>
<meta charset="utf-8">
<title>Bayline Premier Motors – Business Card</title>
<link href="https://fonts.googleapis.com/css2?family=Michroma&family=Exo+2:wght@500&family=Roboto:wght@400;500&display=swap" rel="stylesheet">
<style>
  :root {
    --stage: #d9d6d1;
    --card-dark: #141414;
    --card-dark-2: #262626;
    --red: #e3151b;
    --white: #f4f4f4;
    --silver: #c9c9c9;
    --paper: #ffffff;
  }
  * { margin: 0; padding: 0; box-sizing: border-box; }
  html, body { width: 900px; height: 1200px; overflow: hidden; }
  body { background: var(--stage); position: relative; font-family: "Roboto", sans-serif; }

  .card {
    position: absolute; left: 88px; width: 734px; height: 428px;
    border-radius: 24px; overflow: hidden;
    box-shadow: 0 6px 14px rgba(0,0,0,.35);
  }
  .card-front { top: 137px; background: radial-gradient(ellipse at 35% 40%, var(--card-dark-2), var(--card-dark) 75%); }
  .card-back { top: 633px; background: var(--paper); }

  .wordmark { position: absolute; left: 49px; top: 66px; font-family: "Michroma", sans-serif; color: var(--red); }
  .wordmark-main { font-size: 34px; line-height: 1; letter-spacing: 1px; }
  .wordmark-sub { font-size: 15px; letter-spacing: 6px; margin-top: 10px; }

  .person { position: absolute; left: 49px; top: 232px; }
  .person-name { font-family: "Exo 2", sans-serif; font-weight: 500; font-size: 25px; letter-spacing: 2px; color: var(--white); }
  .person-role { font-family: "Exo 2", sans-serif; font-weight: 500; font-size: 16px; letter-spacing: 1px; color: var(--red); margin-top: 2px; }

  .contact { position: absolute; left: 0; top: 293px; list-style: none; }
  .contact-item { display: flex; align-items: center; height: 24px; margin-bottom: 9px; }
  .contact-bar { width: 44px; height: 24px; background: var(--red); }
  .contact-icon { width: 24px; height: 24px; background: var(--red); margin-left: 6px; display: flex; align-items: center; justify-content: center; }
  .contact-text { margin-left: 10px; font-size: 19px; color: var(--white); }
  .contact-text.email { font-size: 17px; }
  .licence { position: absolute; left: 49px; top: 367px; font-size: 15px; font-weight: 500; color: var(--white); }

  .brand-mark { position: absolute; display: flex; align-items: center; font-family: "Michroma", sans-serif; }
  .brand-dot { border-radius: 50%; background: var(--red); flex: none; }
  .brand-mark-front { left: 470px; top: 180px; gap: 18px; color: var(--white); font-size: 52px; }
  .brand-mark-front .brand-dot { width: 30px; height: 30px; }

  .band { position: absolute; left: 0; width: 100%; background: linear-gradient(180deg, var(--card-dark-2), var(--card-dark)); }
  .band-top { top: 0; height: 70px; border-bottom: 10px solid var(--silver); box-sizing: content-box; }
  .band-bottom { bottom: 0; height: 71px; border-top: 10px solid var(--silver); box-sizing: content-box; }
  .brand-mark-back { left: 0; right: 0; top: 182px; justify-content: center; gap: 14px; color: var(--card-dark-2); font-size: 40px; }
  .brand-mark-back .brand-dot { width: 22px; height: 22px; }
</style>
</head>
<body>
  <section class="card card-front" aria-label="Card front">
    <div class="wordmark">
      <div class="wordmark-main">BAYLINE</div>
      <div class="wordmark-sub">PREMIER MOTORS</div>
    </div>

    <div class="person">
      <div class="person-name">MARCUS T HOLLOWAY</div>
      <div class="person-role">OWNER</div>
    </div>

    <ul class="contact">
      <li class="contact-item">
        <span class="contact-bar"></span>
        <span class="contact-icon">
          <svg width="14" height="14" viewBox="0 0 24 24" aria-hidden="true"><path fill="#fff" d="M6.6 10.8a15.1 15.1 0 0 0 6.6 6.6l2.2-2.2c.3-.3.7-.4 1-.2 1.1.4 2.3.6 3.6.6.6 0 1 .4 1 1V20c0 .6-.4 1-1 1A17 17 0 0 1 3 4c0-.6.4-1 1-1h3.5c.6 0 1 .4 1 1 0 1.3.2 2.5.6 3.6.1.3 0 .7-.2 1z"/></svg>
        </span>
        <span class="contact-text">(555) 417-3860</span>
      </li>
      <li class="contact-item">
        <span class="contact-bar"></span>
        <span class="contact-icon">
          <svg width="14" height="12" viewBox="0 0 24 20" aria-hidden="true"><rect x="1" y="2" width="22" height="16" fill="#fff"/><path d="M1 2l11 9 11-9" fill="none" stroke="#e3151b" stroke-width="2"/></svg>
        </span>
        <span class="contact-text email">baypremmotors@mailbox-example.net</span>
      </li>
    </ul>
    <div class="licence">DEALER LIC # 48261</div>

    <div class="brand-mark brand-mark-front"><span class="brand-dot"></span><span>BPM</span></div>
  </section>

  <section class="card card-back" aria-label="Card back">
    <div class="band band-top"></div>
    <div class="brand-mark brand-mark-back"><span class="brand-dot"></span><span>BPM</span></div>
    <div class="band band-bottom"></div>
  </section>
</body>
</html>
```